Corvane Global Treks Facebook Page

I would like to have a very professional and unique Facebook page for my business
www.corvaneglobaltreks.com

```html
<!DOCTYPE html>
<html lang="en">
<head>
<meta charset="utf-8">
<title>Corvane Global Treks – Facebook Cover</title>
<link rel="stylesheet" href="https://fonts.googleapis.com/css2?family=Montserrat:wght@700;800&family=Oswald:wght@500&family=Open+Sans:wght@600;700&display=swap">
<style>
  :root {
    --page-bg: #e4e4e4;
    --white: #ffffff;
    --teal: #2a7d85;
    --ink: #222222;
    --grey-text: #555555;
    --avatar: #383838;
    --sky: #c3cfd2;
    --peak-glow: #eabca2;
    --ridge: #2c3759;
    --lake: #8ea3bb;
    --reflection: #c9a68c;
    --deep-water: #3a4a6c;
  }
  html, body {
    margin: 0;
    width: 1200px;
    height: 1200px;
    overflow: hidden;
    background: var(--page-bg);
  }
  .cover {
    position: absolute;
    left: 40px;
    top: 348px;
    width: 1120px;
    height: 504px;
    display: block;
  }
  .brand-name { font-family: "Montserrat", sans-serif; font-weight: 700; fill: var(--teal); }
  .headline { font-family: "Montserrat", sans-serif; font-weight: 800; fill: var(--teal); }
  .tagline { font-family: "Oswald", sans-serif; font-weight: 500; fill: var(--teal); }
  .site-url { font-family: "Open Sans", sans-serif; font-weight: 600; fill: var(--ink); }
  .page-name { font-family: "Open Sans", sans-serif; font-weight: 700; fill: var(--grey-text); }
</style>
</head>
<body>
<svg class="cover" viewBox="0 0 1288 580" xmlns="http://www.w3.org/2000/svg">
  <defs>
    <linearGradient id="landscape-tones" x1="0" y1="0" x2="0" y2="1">
      <stop offset="0" stop-color="var(--sky)"/>
      <stop offset="0.22" stop-color="var(--peak-glow)"/>
      <stop offset="0.48" stop-color="var(--ridge)"/>
      <stop offset="0.62" stop-color="var(--lake)"/>
      <stop offset="0.8" stop-color="var(--reflection)"/>
      <stop offset="1" stop-color="var(--deep-water)"/>
    </linearGradient>
  </defs>

  <rect class="cover-base" x="0" y="0" width="1288" height="580" fill="var(--white)"/>

  <rect class="hero-photo" x="0" y="0" width="1288" height="478" fill="url(#landscape-tones)"
        role="img" aria-label="Photo of snow-capped mountains at sunrise reflected in a calm lake"/>

  <polygon class="chevron-veil" points="700,0 790,0 662,255 790,478 700,478 572,255"
           fill="var(--white)" opacity="0.3"/>
  <polygon class="chevron-line" points="790,0 806,0 678,255 806,478 790,478 662,255"
           fill="var(--white)"/>

  <polygon class="info-panel" points="882,0 1288,0 1288,478 867,478 754,255" fill="var(--white)"/>

  <circle class="brand-dot" cx="944" cy="80" r="36" fill="var(--teal)"/>
  <text class="brand-name" font-size="27">
    <tspan x="992" y="74">Corvane</tspan>
    <tspan x="992" y="106">Global Treks</tspan>
  </text>

  <text class="headline" x="1050" y="210" font-size="38" text-anchor="middle" letter-spacing="1">VISIT THE TOP OF</text>
  <text class="headline" x="1050" y="282" font-size="58" text-anchor="middle" letter-spacing="2">THE WORLD</text>
  <text class="tagline" x="1050" y="334" font-size="34" text-anchor="middle">CHALLENGE YOURSELF</text>

  <text class="site-url" x="1060" y="448" font-size="18" text-anchor="middle">www.corvaneglobaltreks.com</text>

  <rect class="profile-picture" x="62" y="320" width="248" height="246" fill="var(--avatar)"/>
  <text class="page-name" x="370" y="534" font-size="34">Company Name</text>
</svg>
</body>
</html>
```